Presentation Folder for A New Home Construction Company

We need a Presentation Folder for a new home construction company based in Perth, Australia. It's called Korvale Homes and specialises in building quality homes that are affordable and people want to live in. The target market is first-home buyers.

We've rebranded the website (www.korvalehomes.com.au) and are looking to update our presentation folder to match it. We want red, white, grey and black as the colour palette, and some designs with transparent photos included but overall a minimalistic approach that aligns with our new website and vehicles.

I've attached an image of our updated car wrap, can you please follow this as a guide?

I've also attached our logo, style guide and past presentation folder for reference.

Please also include:

"Plan Well, Settle In, Stay On" - refer to the previous presentation folder.

Target Market(s)

First Home Buyers

Industry/Entity Type

New Home Construction

Font styles to use
Sans Serif
Other font styles liked:
• Monserrat

Colors
EB3D1F
EC4F4E
F09395
F8D3D4
FCEDEE

Requirements
Must have
• Monserrat or Open Sans Font and Include the colours from the attached brand guide, the contact details and address,
Nice to have
• some with a photo feature - but not the main component, very minimal.
Should not have
• Too many elements, (refer to previous folder attachment) animations or graphics.

```html
<!DOCTYPE html>
<html lang="en">
<head>
<meta charset="utf-8">
<title>Korvale Homes – Presentation Folder</title>
<link rel="stylesheet" href="https://fonts.googleapis.com/css2?family=Montserrat:wght@300;400;600;700;800&display=swap">
<style>
  :root {
    --backdrop: #e6e7e7;
    --paper: #ffffff;
    --fold: #b9b9b9;
    --brand-red: #ec1c24;
    --ink: #050708;
    --charcoal: #3a3a3c;
    --white: #ffffff;
  }
  html, body {
    margin: 0;
    width: 1200px;
    height: 894px;
    overflow: hidden;
    background: var(--backdrop);
    font-family: "Montserrat", sans-serif;
  }
  .canvas {
    position: relative;
    width: 1200px;
    height: 894px;
  }
  .folder-dieline {
    position: absolute;
    left: 0;
    top: 0;
  }
  .tagline {
    position: absolute;
    left: 387px;
    top: 278px;
    margin: 0;
    font-size: 25px;
    line-height: 30px;
    color: var(--ink);
    letter-spacing: 0.2px;
  }
  .tagline .line { display: block; white-space: nowrap; }
  .tagline strong { font-weight: 700; color: var(--brand-red); }
  .tagline .soft { font-weight: 300; }

  .brand-name {
    position: absolute;
    left: 800px;
    top: 284px;
    width: 150px;
    text-align: center;
    font-weight: 800;
    color: var(--charcoal);
    font-size: 22px;
    line-height: 28px;
    letter-spacing: 3px;
  }
  .brand-name .mark {
    display: block;
    width: 14px;
    height: 14px;
    margin: 0 auto 10px;
    background: var(--brand-red);
  }

  .contact {
    position: absolute;
    left: 387px;
    top: 549px;
    color: var(--white);
    font-size: 7.4px;
    line-height: 9.2px;
    font-weight: 400;
    font-style: normal;
  }
  .contact p { margin: 0; white-space: nowrap; }
  .contact .address { margin-top: 9px; }
  .contact b { font-weight: 700; }

  .web-address {
    position: absolute;
    left: 695px;
    top: 592px;
    color: var(--white);
    font-size: 9.6px;
    font-weight: 700;
    letter-spacing: 0.2px;
  }
</style>
</head>
<body>
<main class="canvas">
  <svg class="folder-dieline" width="1200" height="894" viewBox="0 0 1200 894" aria-hidden="true">
    <path d="M156 98 H265 V649 L131 646 V123 A25 25 0 0 1 156 98 Z" fill="var(--paper)"/>
    <rect x="265" y="98" width="804" height="551" fill="var(--paper)"/>
    <path d="M272 649 V657 L310 701 L296 716 A6 6 0 0 0 295 724 L320 756 A7 7 0 0 0 330 757 L347 745 L392 796 H600 A60 60 0 0 0 660 736 V649 Z" fill="var(--paper)"/>
    <line x1="265.5" y1="98" x2="265.5" y2="498" stroke="var(--fold)" stroke-width="0.6"/>
    <line x1="660.5" y1="98" x2="660.5" y2="498" stroke="var(--fold)" stroke-width="0.6"/>
    <polygon points="265,505 698,505 973,649 265,649" fill="var(--ink)"/>
    <polygon points="265,498 703,498 1069,649 973,649 698,505 265,505" fill="var(--brand-red)"/>
  </svg>

  <h1 class="tagline">
    <span class="line"><strong>PLAN</strong> <span class="soft">WELL…</span></span>
    <span class="line"><strong>SETTLE</strong> <span class="soft">IN…</span></span>
    <span class="line"><strong>STAY ON</strong><span class="soft">.</span></span>
  </h1>

  <div class="brand-name">
    <span class="mark"></span>
    KORVALE<br>HOMES
  </div>

  <address class="contact">
    <p><b>t</b> 08 9400 2716</p>
    <p><b>f</b> 08 9400 2717</p>
    <p><b>e</b> hello@korvalehomes.com.au</p>
    <p class="address">14 Harwin Street, Larrow Vale,<br>WA 6099, PO Box 2280,<br>Larrow Vale WA 6998</p>
  </address>

  <div class="web-address">korvalehomes.com.au</div>
</main>
</body>
</html>
```